Bref créative
Business Card, Stationary, etc. for a plastic surgeon's office
Brennholt Clinic (Plastic & Reconstructive Surgery)
Use standard fonts
Play with the fonts to see what looks best.
Professional
Gregory T. Brennholt, DO
Plastic Surgeon
475 Corwin Haley Blvd, Ste. 260
Panama City Beach, FL 32407
(Tollmead Business Park)
850-GET-TRIM (850-438-8746)
850-438-FAX5 (850-438-3295)
drbrennholt@brennholtclinic.example
www.brennholtclinic.example
This card, stationary, etc. should look clean and professional with my existing logo purchased from a designer using this sight.
I would like the back of the business card to contain the logo (i.e. Brennholt Clinic in larger letters with logo between the two words with Plastic & Reconstructive Surgery written below the main title with smaller font). Thanks and good luck!!!
logo vector file

```html
<!DOCTYPE html>
<html lang="en">
<head>
<meta charset="utf-8">
<title>Brennholt Clinic – Business Card</title>
<link href="https://fonts.googleapis.com/css2?family=Montserrat:wght@300;400;500&display=swap" rel="stylesheet">
<style>
  :root {
    --backdrop: #e4e4e6;
    --paper: #fbfbfa;
    --gold: #c9a25a;
    --gold-deep: #b08a45;
    --ink: #5b5b5b;
    --night: #141414;
    --white: #ffffff;
  }
  * { box-sizing: border-box; margin: 0; padding: 0; }
  html, body {
    width: 1200px; height: 838px; overflow: hidden;
    background: var(--backdrop);
    font-family: "Montserrat", Arial, sans-serif;
  }
  .canvas {
    width: 1200px; height: 838px;
    display: flex; flex-direction: column;
    align-items: center; justify-content: center; gap: 36px;
  }
  .card {
    position: relative;
    width: 640px; height: 366px;
    box-shadow: 0 10px 28px rgba(0,0,0,0.18);
    overflow: hidden;
  }
  /* Front */
  .card--front { background: var(--paper); }
  .name-band {
    position: absolute; left: 0; right: 0; top: 48px; height: 70px;
    background: var(--gold);
    display: flex; flex-direction: column; align-items: center; justify-content: center;
    padding-left: 110px;
  }
  .name-band .doctor-name {
    color: var(--white); font-weight: 500; font-size: 19px; letter-spacing: 0.3px;
  }
  .name-band .doctor-title {
    color: var(--white); font-weight: 300; font-size: 10px; letter-spacing: 0.5px; margin-top: 3px;
  }
  .wordmark {
    position: absolute; left: 0; right: 0;
    display: flex; flex-direction: column; align-items: center;
    color: var(--gold);
  }
  .card--front .wordmark { top: 134px; }
  .wordmark .clinic-name {
    display: flex; align-items: center; gap: 12px;
    font-weight: 400; font-size: 38px; letter-spacing: 1px;
  }
  .wordmark .mark-dot {
    width: 10px; height: 10px; border-radius: 50%; background: var(--gold);
  }
  .wordmark .specialty {
    font-weight: 400; font-size: 11px; letter-spacing: 3.2px; text-transform: uppercase; margin-top: 4px;
  }
  .details {
    position: absolute; top: 236px; left: 46px; right: 40px;
    display: flex; font-size: 11.5px; font-weight: 400; color: var(--ink); line-height: 1.55;
  }
  .address { width: 245px; text-align: right; padding-right: 16px; }
  .divider { width: 1px; background: var(--gold); align-self: stretch; }
  .contact { padding-left: 16px; }
  .contact .label { color: var(--gold-deep); font-weight: 500; display: inline-block; width: 16px; }
  .website {
    position: absolute; right: 40px; bottom: 26px;
    font-size: 13px; color: var(--ink); letter-spacing: 0.3px;
  }
  /* Back */
  .card--back { background: var(--night); }
  .card--back .wordmark { top: 132px; }
  .card--back .clinic-name { font-size: 46px; }
  .card--back .specialty { font-size: 13px; letter-spacing: 3.8px; }
</style>
</head>
<body>
<main class="canvas">
  <section class="card card--front" aria-label="Business card front">
    <div class="name-band">
      <span class="doctor-name">Gregory T. Brennholt, DO</span>
      <span class="doctor-title">Plastic Surgeon</span>
    </div>
    <div class="wordmark">
      <div class="clinic-name"><span>Brennholt</span><span class="mark-dot"></span><span>Clinic</span></div>
      <div class="specialty">Plastic &amp; Reconstructive Surgery</div>
    </div>
    <div class="details">
      <div class="address">
        475 Corwin Haley Blvd, Ste. 260<br>
        Panama City Beach, FL 32407<br>
        (Tollmead Business Park)
      </div>
      <div class="divider"></div>
      <div class="contact">
        <div><span class="label">T:</span>850-GET-TRIM (850-438-8746)</div>
        <div><span class="label">F:</span>850-438-FAX5 (850-438-3295)</div>
        <div><span class="label">E:</span>drbrennholt@brennholtclinic.example</div>
      </div>
    </div>
    <div class="website">www.brennholtclinic.example</div>
  </section>

  <section class="card card--back" aria-label="Business card back">
    <div class="wordmark">
      <div class="clinic-name"><span>Brennholt</span><span class="mark-dot"></span><span>Clinic</span></div>
      <div class="specialty">Plastic &amp; Reconstructive Surgery</div>
    </div>
  </section>
</main>
</body>
</html>
```